Cybersecurity company is looking for business card.

I need a business card design for our company, we are a cybersecurity company providing advance technology to protect agains any kind of malware. We need a fresh modern design it should communicate modern, technology and growth.

Target Market(s)

Business to business

Industry/Entity Type

Business

Contact Information for Business Card

Should have location, address, fax, mobile, phone, email and website.

Requirements
Must have
• Must follow company's logo color and style. Must have the company's log on its.

```html
<!DOCTYPE html>
<html lang="en">
<head>
<meta charset="utf-8">
<title>Vexora Business Card</title>
<link rel="stylesheet" href="https://fonts.googleapis.com/css2?family=Michroma&display=swap">
<style>
  :root {
    --page-bg: #e9e7e4;
    --card-red-light: #b5121b;
    --card-red: #7e0a10;
    --card-red-dark: #3a0306;
    --band-black: #120203;
    --accent-red: #d41a22;
    --text-white: #ffffff;
    --text-soft: #f1d9da;
  }
  * { box-sizing: border-box; margin: 0; padding: 0; }
  html, body {
    width: 1200px; height: 900px; overflow: hidden;
    background: var(--page-bg);
    font-family: "Michroma", "Arial", sans-serif;
  }
  .canvas {
    width: 1200px; height: 900px;
    display: flex; flex-direction: column;
    align-items: center; justify-content: center;
    gap: 40px;
  }
  .card {
    position: relative;
    width: 560px; height: 320px;
    border-radius: 30px;
    overflow: hidden;
    background: radial-gradient(ellipse at 50% 30%, var(--card-red-light) 0%, var(--card-red) 45%, var(--card-red-dark) 100%);
    box-shadow: 0 10px 24px rgba(0,0,0,0.22);
    color: var(--text-white);
  }
  .card-waves { position: absolute; inset: 0; }
  .brand-name {
    position: absolute;
    font-weight: 400;
    color: var(--text-white);
    letter-spacing: 1px;
    line-height: 1;
  }
  .card-front .brand-name { top: 56px; left: 0; right: 0; text-align: center; font-size: 46px; }
  .card-back .brand-name { top: 50%; left: 0; right: 0; transform: translateY(-50%); text-align: center; font-size: 64px; }

  .person {
    position: absolute;
    top: 136px; right: 295px;
    text-align: right;
  }
  .person-name { font-size: 14px; letter-spacing: 1px; text-transform: uppercase; }
  .person-title { font-size: 9px; margin-top: 6px; color: var(--text-soft); text-transform: uppercase; letter-spacing: 1px; }
  .person-address { font-size: 9px; margin-top: 12px; line-height: 1.6; text-transform: uppercase; letter-spacing: 0.5px; }

  .divider {
    position: absolute;
    left: 280px; top: 136px;
    width: 1px; height: 96px;
    background: var(--text-soft);
    opacity: 0.8;
  }
  .contacts {
    position: absolute;
    top: 136px; left: 292px;
    list-style: none;
    font-size: 9.5px;
    line-height: 19px;
    text-transform: uppercase;
    letter-spacing: 0.5px;
  }
  .contacts li { display: flex; align-items: center; gap: 6px; white-space: nowrap; }
  .contact-icon { width: 11px; height: 11px; flex: none; }
</style>
</head>
<body>
<main class="canvas">

  <section class="card card-front" aria-label="Business card front">
    <svg class="card-waves" viewBox="0 0 560 320" width="560" height="320" aria-hidden="true">
      <path d="M0 232 C 120 236, 230 280, 340 298 C 430 310, 500 312, 560 312 L560 320 L0 320 Z" fill="var(--band-black)"/>
      <path d="M0 218 C 120 222, 230 266, 340 284 C 430 298, 500 300, 560 300 L560 306 C 500 306, 430 304, 340 292 C 230 276, 120 234, 0 230 Z" fill="var(--accent-red)"/>
      <path d="M0 268 C 110 272, 200 300, 300 320 L0 320 Z" fill="var(--accent-red)" opacity="0.35"/>
    </svg>

    <div class="brand-name">vexora</div>

    <div class="person">
      <p class="person-name">Alan Ward</p>
      <p class="person-title">Owner - C.E.O</p>
      <p class="person-address">Suite # 418, Kell Bldg,<br>NY 10482</p>
    </div>

    <div class="divider"></div>

    <ul class="contacts">
      <li><svg class="contact-icon" viewBox="0 0 12 12"><circle cx="6" cy="6" r="6" fill="#fff"/><path d="M4 3.2 L5 4.6 L4.5 5.3 C5 6.3 5.7 7 6.7 7.5 L7.4 7 L8.8 8 L8.2 9 C6 9 3 6 3 3.8 Z" fill="var(--card-red)"/></svg>214-555-0187</li>
      <li><svg class="contact-icon" viewBox="0 0 12 12"><circle cx="6" cy="6" r="6" fill="#fff"/><rect x="4" y="2.5" width="4" height="7" rx="0.8" fill="var(--card-red)"/></svg>214-555-0162</li>
      <li><svg class="contact-icon" viewBox="0 0 12 12"><circle cx="6" cy="6" r="6" fill="#fff"/><rect x="3" y="5" width="6" height="4" fill="var(--card-red)"/><rect x="4" y="3" width="4" height="2" fill="var(--card-red)"/></svg>214-555-0143</li>
      <li><svg class="contact-icon" viewBox="0 0 12 12"><circle cx="6" cy="6" r="6" fill="#fff"/><rect x="3" y="4" width="6" height="4.2" fill="var(--card-red)"/><path d="M3 4 L6 6.3 L9 4" stroke="#fff" stroke-width="0.7" fill="none"/></svg>name@vexoradefense.com</li>
      <li><svg class="contact-icon" viewBox="0 0 12 12"><circle cx="6" cy="6" r="6" fill="#fff"/><circle cx="6" cy="6" r="3.2" fill="none" stroke="var(--card-red)" stroke-width="0.9"/><path d="M2.8 6 H9.2 M6 2.8 V9.2" stroke="var(--card-red)" stroke-width="0.8"/></svg>www.vexoradefense.com</li>
    </ul>
  </section>

  <section class="card card-back" aria-label="Business card back">
    <div class="brand-name">vexora</div>
  </section>

</main>
</body>
</html>
```